I am looking for a modern style design for a podcast cover art.
Titled: Open Horizon with R.T. Pellow
colors to stay in the grays, reds, blacks, white, gold, and maybe blues if it fits well. I attached a mock up of what we are going for and a current podcast cover we drew inspiration from.
Colors
3276b5
ec1f27
f04a50
1b1b1b
474747
919191
d2d2d2

```html
<!DOCTYPE html>
<html lang="en">
<head>
<meta charset="utf-8">
<title>Open Horizon with R.T. Pellow — Podcast Cover</title>
<link href="https://fonts.googleapis.com/css2?family=Montserrat:wght@400;700&display=swap" rel="stylesheet">
<style>
  :root {
    --brand-blue: #2e4bd0;
    --brand-red: #d40808;
    --ink: #1b1b1b;
    --frame-line: #474747;
    --paper: #ffffff;
    --photo-light: #919191;
    --photo-dark: #1b1b1b;
  }
  html, body {
    margin: 0;
    padding: 0;
    width: 1200px;
    height: 1200px;
    overflow: hidden;
    background: var(--paper);
  }
  .cover {
    position: relative;
    width: 1200px;
    height: 1200px;
    font-family: "Montserrat", sans-serif;
  }
  .cover-art {
    position: absolute;
    inset: 0;
  }
  .title {
    position: absolute;
    margin: 0;
    font-weight: 700;
    font-size: 110px;
    line-height: 1;
    letter-spacing: -1px;
    text-transform: uppercase;
    white-space: nowrap;
  }
  .title-first {
    left: 252px;
    top: 280px;
    color: var(--brand-blue);
  }
  .title-second {
    left: 240px;
    top: 376px;
    color: var(--brand-red);
  }
  .host-rule {
    position: absolute;
    left: 251px;
    top: 863px;
    width: 351px;
    height: 0;
    border-top: 1.5px solid var(--ink);
  }
  .host-name {
    position: absolute;
    left: 251px;
    top: 888px;
    margin: 0;
    font-weight: 400;
    font-size: 28px;
    line-height: 1;
    letter-spacing: 0.16em;
    color: var(--ink);
    text-transform: uppercase;
    white-space: nowrap;
  }
</style>
</head>
<body>
<main class="cover">
  <svg class="cover-art" width="1200" height="1200" viewBox="0 0 1200 1200" xmlns="http://www.w3.org/2000/svg">
    <defs>
      <linearGradient id="host-photo-tone" x1="0" y1="0" x2="0" y2="1">
        <stop offset="0" stop-color="var(--photo-light)"/>
        <stop offset="0.35" stop-color="#474747"/>
        <stop offset="1" stop-color="var(--photo-dark)"/>
      </linearGradient>
    </defs>

    <g class="frame-bands">
      <polygon fill="var(--brand-red)" points="173,173 666,173 699,198 198,198"/>
      <polygon fill="var(--brand-blue)" points="673,173 1027,173 1027,435 998,416 998,198 706,198"/>
      <polygon fill="var(--brand-red)" points="1027,442 1027,1027 998,998 998,423"/>
      <polygon fill="var(--brand-red)" points="173,173 198,198 198,666 173,648"/>
      <polygon fill="var(--brand-blue)" points="173,654 198,672 198,998 474,998 428,1027 173,1027"/>
      <polygon fill="var(--brand-red)" points="482,998 998,998 1027,1027 436,1027"/>
    </g>

    <rect class="frame-panel" x="198" y="198" width="800" height="800" fill="var(--paper)" stroke="var(--frame-line)" stroke-width="3"/>

    <rect class="host-photo" role="img" aria-label="Black-and-white photo of the host in a tuxedo and bow tie, pointing to the left"
      x="780" y="344" width="247" height="683" fill="url(#host-photo-tone)"/>
  </svg>

  <h1 class="title title-first">Open</h1>
  <p class="title title-second">Horizon</p>

  <div class="host-rule"></div>
  <p class="host-name">With R.T. Pellow</p>
</main>
</body>
</html>
```